Letterhead Design Project

Please do not submit designs until I upload file-

Requirements
Must have
• clean lines and font- easy to read; consistent with the design on the business card
Does not use too much of the real estate of the size of the paper

```html
<!DOCTYPE html>
<html lang="en">
<head>
<meta charset="utf-8">
<title>The Alderpeak Foundation — Letterhead</title>
<link rel="stylesheet" href="https://fonts.googleapis.com/css2?family=Montserrat:wght@400;500;700&display=swap">
<style>
  :root {
    --backdrop: #e9e9ea;
    --paper: #f4f4f5;
    --navy: #1f416f;
    --ink: #3c4250;
    --faint: #c6ccd8;
    --band-text: #ffffff;
  }
  * { margin: 0; padding: 0; box-sizing: border-box; }
  html, body {
    width: 1200px;
    height: 795px;
    overflow: hidden;
    background: var(--backdrop);
    font-family: "Montserrat", sans-serif;
  }
  .canvas {
    width: 1200px;
    height: 795px;
    display: flex;
    align-items: center;
    justify-content: center;
  }
  .letterhead {
    position: relative;
    width: 584px;
    height: 755px;
    background: var(--paper);
    box-shadow: 0 6px 18px rgba(0, 0, 0, 0.12);
  }
  .brand {
    position: absolute;
    top: 52px;
    left: 48px;
    display: flex;
    align-items: center;
    gap: 8px;
  }
  .brand-square {
    width: 16px;
    height: 16px;
    background: var(--navy);
  }
  .brand-name {
    color: var(--navy);
    font-weight: 700;
    font-size: 11px;
    line-height: 1.05;
    letter-spacing: 0.02em;
    text-transform: uppercase;
  }
  .contact {
    position: absolute;
    top: 50px;
    right: 48px;
    list-style: none;
    color: var(--ink);
    font-size: 7.5px;
    letter-spacing: 0.16em;
    line-height: 1.9;
  }
  .contact li { display: flex; align-items: center; gap: 7px; }
  .contact .icon { width: 8px; height: 8px; flex: none; }
  .contact .indent { padding-left: 0; }
  .watermark {
    position: absolute;
    top: 260px;
    left: 50%;
    width: 220px;
    height: 220px;
    margin-left: -110px;
    background: var(--faint);
    opacity: 0.55;
  }
  .footer-band {
    position: absolute;
    left: 0;
    right: 0;
    bottom: 0;
    height: 40px;
    background: var(--navy);
    display: flex;
    align-items: center;
    justify-content: flex-end;
    padding-right: 48px;
  }
  .website {
    color: var(--band-text);
    font-size: 10px;
    font-weight: 500;
    letter-spacing: 0.2em;
  }
</style>
</head>
<body>
<main class="canvas">
  <article class="letterhead">
    <header class="brand">
      <span class="brand-square"></span>
      <span class="brand-name">The<br>Alderpeak<br>Foundation</span>
    </header>

    <ul class="contact">
      <li>4180 Larkspur Commons Way, Suite 310</li>
      <li>Cedar Harbor, FL 33921</li>
      <li>
        <svg class="icon" viewBox="0 0 10 10" aria-hidden="true">
          <path d="M2 1h2l1 2.5-1.3 1a5 5 0 0 0 2.3 2.3l1-1.3L9.5 6v2a1 1 0 0 1-1 1A8 8 0 0 1 1 2a1 1 0 0 1 1-1z" fill="none" stroke="#3c4250" stroke-width="0.9"/>
        </svg>
        +1 555-014-2286
      </li>
      <li>
        <svg class="icon" viewBox="0 0 10 10" aria-hidden="true">
          <rect x="0.5" y="2" width="9" height="6" fill="#1f416f"/>
          <path d="M0.5 2l4.5 3.5L9.5 2" fill="none" stroke="#f4f4f5" stroke-width="0.8"/>
        </svg>
        dana.hollis@alderpeakfoundation.org
      </li>
    </ul>

    <div class="watermark" aria-hidden="true"></div>

    <footer class="footer-band">
      <span class="website">www.alderpeakfoundation.org</span>
    </footer>
  </article>
</main>
</body>
</html>
```